Computer Service Provider in Need of New Letterhead Design

We are Larkvale Computer Services, a computer/IT services company that provides IT Support, software, hardware, virus monitoring, etc. in Vermont. We are looking for new letterhead, that is both professional and matches the current theme of our business cards & website.
Please note that we want to include the following information:
www.Larkvale.example
802-555-0147
47 Fernwick Hollow Road, Ashbrook Falls, VT 05999
Responsive Support • Friendly Experts • Reliable Results
I will be attaching our logo along with the business card images.
We would love to have the

```html
<!DOCTYPE html>
<html lang="en">
<head>
<meta charset="utf-8">
<title>Larkvale Computer Services – Letterhead</title>
<link href="https://fonts.googleapis.com/css2?family=Lato:wght@400;700&family=Tinos:wght@400;700&display=swap" rel="stylesheet">
<style>
  :root{
    --backdrop:#6f6f6f;
    --paper:#f8f8f8;
    --brand-blue:#2b5b86;
    --brand-orange:#f29423;
    --ink:#1a1a1a;
    --muted:#4a4a4a;
    --rule:#4f79b0;
  }
  html,body{margin:0;padding:0;width:1200px;height:1200px;overflow:hidden;background:var(--backdrop);}
  .letterhead{
    position:absolute;left:232px;top:50px;width:735px;height:1100px;
    background:var(--paper);
  }
  .edge-bar{position:absolute;left:0;top:0;width:12px;height:1100px;background:var(--brand-blue);}
  .edge-mark{position:absolute;left:18px;top:190px;width:6px;height:170px;background:var(--brand-orange);}
  .brand{
    position:absolute;left:58px;top:44px;display:flex;align-items:center;gap:12px;
  }
  .brand-square{width:44px;height:44px;background:var(--brand-blue);}
  .brand-name{
    font-family:'Lato',sans-serif;font-weight:700;font-size:24px;color:var(--brand-blue);
    letter-spacing:.2px;
  }
  .contact{
    position:absolute;right:54px;top:52px;text-align:right;
    font-family:'Lato',sans-serif;font-size:13.5px;line-height:18px;color:var(--muted);
  }
  .letter{
    position:absolute;left:66px;width:602px;
    font-family:'Tinos','Times New Roman',serif;font-size:14.6px;line-height:17.7px;color:var(--ink);
  }
  .letter p{margin:0;}
  .justify{text-align:justify;}
  .date{top:221px;}
  .recipient{top:292px;}
  .subject{top:399px;font-weight:700;}
  .salutation{top:469px;}
  .para-1{top:506px;}
  .para-2{top:576px;}
  .para-3{top:647px;}
  .closing{top:719px;}
  sup{font-size:9px;line-height:0;}
  .tagline{
    position:absolute;left:0;right:0;top:1014px;text-align:center;
    font-family:'Lato',sans-serif;font-size:14.5px;color:var(--ink);
  }
  .tagline .dot{color:var(--brand-orange);margin:0 4px;}
  .footer-rule{position:absolute;left:47px;width:640px;top:1044px;height:1.5px;background:var(--rule);}
  .address{
    position:absolute;left:0;right:0;top:1053px;text-align:center;
    font-family:'Lato',sans-serif;font-size:14.5px;color:var(--ink);
  }
</style>
</head>
<body>
<div class="letterhead">
  <div class="edge-bar"></div>
  <div class="edge-mark"></div>

  <div class="brand">
    <div class="brand-square"></div>
    <div class="brand-name">Larkvale Computer Services</div>
  </div>

  <div class="contact">802-555-0147<br>www.Larkvale.example</div>

  <div class="letter date"><p>Issuing date: May 5, 2012</p></div>
  <div class="letter recipient">
    <p>Name of employee: Mr. xyz</p>
    <p>Address of employee</p>
    <p>address line 2</p>
  </div>
  <div class="letter subject"><p>Ref: Promotion as an Assistant secretary</p></div>
  <div class="letter salutation"><p>Dear Mr. xyz,</p></div>
  <div class="letter para-1 justify"><p>I have the pleasure to inform you that you have been promoted as assistant secretary in the share department of the company. You are required to take charge of the new assignment on 15<sup>th</sup> May, 2012. Please accept my hearty congratulations on your promotion.</p></div>
  <div class="letter para-2 justify"><p>Your salary scale in the promoted cadre will be Tk. 16,000 and from 15th may, your basic salary will be fixed at Tk. 12,000 in the said scale. You will be entitled to all other allowances as applicable to the staff-II of the company. Other services conditions remain unchanged.</p></div>
  <div class="letter para-3"><p>Please acknowledge receipt of this letter.</p></div>
  <div class="letter closing"><p>Yours sincerely,</p></div>

  <div class="tagline">Responsive Support<span class="dot">•</span>Friendly Experts<span class="dot">•</span>Reliable Results</div>
  <div class="footer-rule"></div>
  <div class="address">47 Fernwick Hollow Road, Ashbrook Falls, VT 05999</div>
</div>
</body>
</html>
```